tile distributor needs a new logo and packaging designe

"VARLISK TILE & STONE LTD'' in Canada needs great logo and a graphic design for a cardboard box package for the ceramic tiles. For inspiration you can use the logo from our sister's company, www.varlisk-example.de.
In regards to the cardboard package for the ceramic tiles it should include the VARLISK new logo on white cardboard background.
The box has to have the following info:
-Company name (with slogan "ARCHITECTURAL SOLUTIONS" or similar)
-Nominal size of the tiles (we need packages for 30cm x 60cm, 60cm x 60cm,and 30cm x 90cm) with table: nominal thickness, #pieces per box and MQ/SFT per box
-product description "RECTIFIED PORCELAIN TILE"
-made in china (not too visible, small letters)
-CE sign
-Attention text:"Before tile setting, please verify...." (see the attachment)
-Emission in indoor air sign
-and the hole on the front page (the color of the tile should be visible)
All text will be translated in 3 languages (German, English and Serbian)
I have attached some samples of the competitor"s packages and our current box for your reference.
Updates
I have increased the budget for CND$100 for my project and I hope that now it will be more atractiv for designers.
Looking forward to seeing your fresh ideas.
Reason: I have just increased the budget for this project therefore I am extending the deadline.
Hope this will help to get the great design for my company logo and packaging.
Graphic Design

```html
<!DOCTYPE html>
<html lang="en">
<head>
<meta charset="utf-8">
<title>VARLISK Rectified Porcelain Tile – Box Front</title>
<link href="https://fonts.googleapis.com/css2?family=Open+Sans:wght@400;600;700;800&display=swap" rel="stylesheet">
<style>
  :root {
    --page-bg: #d9d9d9;
    --box-white: #ffffff;
    --slate: #4c6469;
    --band: #5f7a80;
    --band-line: #dfe8ea;
    --brand-green: #3aa860;
    --brand-blue: #8fb7e6;
    --tile-light: #ecdcc0;
    --tile-mid: #d9c19a;
    --tile-vein: #c9a064;
    --mark-grey: #9aa3a6;
    --badge-blue: #5aa7d6;
  }
  * { box-sizing: border-box; margin: 0; padding: 0; }
  html, body {
    width: 1200px; height: 876px; overflow: hidden;
    background: linear-gradient(#e6e6e6, #bdbdbd);
    font-family: "Open Sans", Arial, sans-serif;
  }
  .box-front {
    position: absolute; left: 120px; top: 70px;
    width: 960px; height: 480px;
    background: var(--box-white);
    box-shadow: 0 6px 24px rgba(0,0,0,.18);
  }
  .brand { position: absolute; left: 52px; top: 40px; width: 220px; text-align: center; }
  .brand-row { display: flex; align-items: center; justify-content: center; gap: 10px; }
  .brand-dot { width: 34px; height: 34px; border-radius: 50%; background: var(--brand-green); }
  .brand-name { font-size: 46px; font-weight: 600; color: var(--slate); letter-spacing: 1px; line-height: 1; }
  .brand-slogan { margin-top: 10px; font-size: 14px; font-weight: 700; color: var(--slate); line-height: 1.2; }
  .product-title {
    position: absolute; right: 40px; top: 36px; text-align: right;
    font-size: 42px; font-weight: 800; color: var(--slate); line-height: 1.05; letter-spacing: .5px;
  }
  .tile-window { position: absolute; left: 360px; top: 150px; }
  .info-band {
    position: absolute; left: 0; right: 0; top: 320px; height: 140px;
    background: var(--band);
  }
  .spec-table {
    position: absolute; left: 22px; top: 18px; border-collapse: collapse;
    color: var(--band-line); font-size: 13px;
  }
  .spec-table td { border: 1px solid var(--band-line); padding: 2px 8px; height: 22px; }
  .spec-table td:first-child { width: 148px; }
  .spec-table td:last-child { width: 56px; text-align: center; }
  .nominal-size { position: absolute; right: 40px; top: 40px; color: #fff; font-size: 22px; font-weight: 600; }
  .nominal-size strong { font-size: 40px; font-weight: 700; margin-left: 6px; }
  .origin { position: absolute; right: 40px; bottom: 14px; color: #fff; font-size: 13px; }

  .box-side {
    position: absolute; left: 120px; top: 600px;
    width: 960px; height: 120px;
    background: var(--box-white);
    box-shadow: 0 6px 24px rgba(0,0,0,.18);
    display: flex; align-items: center; padding: 0 40px; gap: 28px;
  }
  .emission-badge { width: 150px; height: 70px; border: 2px solid var(--badge-blue); border-radius: 3px; }
  .side-title { font-size: 24px; font-weight: 800; color: var(--band); line-height: 1.05; width: 260px; }
  .conformity-mark { width: 46px; height: 34px; border-radius: 4px; background: var(--mark-grey); margin-left: 40px; }
  .side-brand { margin-left: auto; display: flex; align-items: center; gap: 18px; }
  .side-slogan { font-size: 15px; font-weight: 700; font-style: normal; color: var(--band); text-align: center; line-height: 1.15; }
  .side-name { display: flex; align-items: center; gap: 8px; font-size: 30px; font-weight: 600; color: var(--slate); }
  .side-name .brand-dot { width: 22px; height: 22px; }
</style>
</head>
<body>
  <section class="box-front">
    <div class="brand">
      <div class="brand-row">
        <span class="brand-dot"></span>
        <span class="brand-name">VARLISK</span>
      </div>
      <p class="brand-slogan">ARCHITECTURAL<br>SOLUTIONS</p>
    </div>

    <h1 class="product-title">RECTIFIED<br>PORCELAIN TILE</h1>

    <svg class="tile-window" width="570" height="170" viewBox="0 0 570 170" role="img" aria-label="Die-cut window showing the beige marble-look porcelain tile inside">
      <defs>
        <linearGradient id="tileSurface" x1="0" y1="0" x2="1" y2="1">
          <stop offset="0" stop-color="var(--tile-light)"/>
          <stop offset=".55" stop-color="var(--tile-mid)"/>
          <stop offset="1" stop-color="var(--tile-light)"/>
        </linearGradient>
      </defs>
      <path d="M0 0 H218 L122 170 H14 Q0 170 0 156 Z" fill="url(#tileSurface)"/>
      <path d="M238 14 Q248 0 258 14 L352 170 H144 Z" fill="url(#tileSurface)"/>
      <path d="M280 0 H570 V170 H382 Z" fill="url(#tileSurface)"/>
    </svg>

    <div class="info-band">
      <table class="spec-table">
        <tr><td>Nominal thickness</td><td>11</td></tr>
        <tr><td>Piesces</td><td>8</td></tr>
        <tr><td>MQ</td><td>0,810</td></tr>
      </table>
      <p class="nominal-size">Nominal size:<strong>30x60</strong></p>
      <p class="origin">made in china</p>
    </div>
  </section>

  <section class="box-side">
    <div class="emission-badge"></div>
    <h2 class="side-title">RECTIFIED<br>PORCELAIN TILE</h2>
    <div class="conformity-mark"></div>
    <div class="side-brand">
      <p class="side-slogan">ARCHITECTURAL<br>SOLUTIONS</p>
      <div class="side-name"><span class="brand-dot"></span>VARLISK</div>
    </div>
  </section>
</body>
</html>
```